need to update our new address on letterhead and business cards. Also open to
a redesign and logo in the near future as we are changing our name. New address is Brambleton Corporate Plaza, 782 Ridgecrest Lane, Larkhaven, ME 06587

Target Market(s)

35-75 yrs of age

Industry/Entity Type

Business

Requirements
Nice to have
• We are a financial firm so this need to look impressive and classy

```html
<!DOCTYPE html>
<html lang="en">
<head>
<meta charset="utf-8">
<title>Aldervane Financial – Business Card</title>
<link rel="stylesheet" href="https://fonts.googleapis.com/css2?family=Source+Sans+3:wght@400;600&display=swap">
<style>
  :root {
    --navy: #0c2348;
    --ink: #2a2a2a;
    --card: #fbfbfb;
    --backdrop: #e6e6e6;
    --backdrop-edge: #d2d2d2;
    --white: #ffffff;
  }
  * { margin: 0; padding: 0; box-sizing: border-box; }
  html, body { width: 1200px; height: 886px; overflow: hidden; }
  body {
    background: radial-gradient(ellipse at 50% 40%, var(--backdrop) 0%, var(--backdrop-edge) 100%);
    font-family: "Source Sans 3", sans-serif;
    position: relative;
  }
  .business-card {
    position: absolute;
    left: 80px; top: 149px;
    width: 1040px; height: 588px;
    background: var(--card);
    box-shadow: 0 6px 18px rgba(0,0,0,0.18);
  }
  .company-name {
    position: absolute;
    top: 128px; left: 0; width: 100%;
    text-align: center;
    font-size: 56px;
    font-weight: 400;
    color: var(--navy);
    letter-spacing: 0.5px;
  }
  .holder { position: absolute; left: 32px; top: 314px; }
  .holder-name { font-size: 30px; font-weight: 600; color: var(--navy); line-height: 38px; }
  .holder-title { font-size: 28px; color: var(--ink); line-height: 38px; }
  .address { position: absolute; left: 32px; top: 438px; font-style: normal; font-size: 28px; line-height: 42px; color: var(--ink); }
  .contact-line {
    position: absolute;
    right: 82px;
    font-size: 28px;
    color: var(--ink);
    text-align: right;
    line-height: 36px;
    white-space: nowrap;
  }
  .contact-line.phone { right: 108px; top: 316px; }
  .contact-line.fax { right: 112px; top: 379px; }
  .contact-line.email { top: 447px; }
  .contact-line.web { top: 507px; }
  .icon-rail { position: absolute; right: 0; top: 303px; width: 66px; }
  .icon-tile {
    position: absolute; left: 0; width: 66px;
    background: var(--navy);
    border-radius: 6px 0 0 6px;
    display: flex; align-items: center; justify-content: center;
  }
  .icon-tile svg { width: 30px; height: 30px; fill: none; stroke: var(--white); stroke-width: 2; }
  .icon-tile .solid { fill: var(--white); stroke: none; }
</style>
</head>
<body>
  <section class="business-card">
    <h1 class="company-name">Aldervane Financial</h1>

    <div class="holder">
      <p class="holder-name">Daniel R. Ashworth, Sr.RFC</p>
      <p class="holder-title">President/CEO</p>
    </div>

    <address class="address">
      Brambleton Corporate Plaza<br>
      782 Ridgecrest Lane<br>
      Larkhaven, ME 06587
    </address>

    <p class="contact-line phone">203-555-0142</p>
    <p class="contact-line fax">203-555-0178</p>
    <p class="contact-line email">DAshworth@AldervaneFinancialSvcs.com</p>
    <p class="contact-line web">www.AldervaneFinancialsvcs.com</p>

    <div class="icon-rail">
      <div class="icon-tile" style="top:0;height:62px">
        <svg viewBox="0 0 32 32" aria-label="Phone"><circle cx="16" cy="16" r="13"/><path d="M11 9c-1.5 1-2 3 0 6.5s5 6 7.5 6.5c1.5.3 2.5-.5 3-1.5l-2.5-2.5-2 1c-1.5-.7-3.5-2.7-4-4l1-2z"/></svg>
      </div>
      <div class="icon-tile" style="top:72px;height:62px">
        <svg viewBox="0 0 32 32" aria-label="Fax"><rect class="solid" x="4" y="9" width="7" height="18" rx="2"/><rect x="13" y="12" width="15" height="15" rx="1.5"/><rect class="solid" x="15" y="5" width="11" height="6"/><circle class="solid" cx="17" cy="17" r="1.3"/><circle class="solid" cx="21" cy="17" r="1.3"/><circle class="solid" cx="25" cy="17" r="1.3"/><circle class="solid" cx="17" cy="22" r="1.3"/><circle class="solid" cx="21" cy="22" r="1.3"/><circle class="solid" cx="25" cy="22" r="1.3"/></svg>
      </div>
      <div class="icon-tile" style="top:141px;height:64px">
        <svg viewBox="0 0 32 32" aria-label="Email"><rect x="4" y="8" width="24" height="16" rx="1.5"/><path d="M4 8l12 10 12-10M4 24l9-8M28 24l-9-8"/></svg>
      </div>
      <div class="icon-tile" style="top:211px;height:53px">
        <svg viewBox="0 0 32 32" aria-label="Website"><circle cx="16" cy="16" r="11"/><ellipse cx="16" cy="16" rx="5" ry="11"/><path d="M5 16h22M7 10h18M7 22h18"/></svg>
      </div>
    </div>
  </section>
</body>
</html>
```